NOTE: I PROVIDED THE INCORRECT LOGO AND ONLY A HANDFUL OF PEOPLE NOTICED THAT IT WAS NOT THE ONE I DESCRIBED. THE LOGO I HAVE NOW ATTACHED MATCHES MY WEBSITE AND THE COLORS ON THE WEBSITE SHOULD BE USED FOR THE CARD.

PLEASE READ THE BUSINESS CARD DETAILS AND PROJECT MUST HAVES CAREFULLY.

I am looking for a business card that is powerful, a bit edgy, and although I work in the corporate world, not too formal. I would like to see designs that use the colors on my website www.brightmoorlane.com. I don't want the card to look washed out so please use shades of those colors that make them "pop". The "vibe" of the card needs to show substance and confidence while also reflecting that we're not your usual consultants.

The focus of my work is turning "people problems" into profits. Those problems could be poor service, an unstable workforce, untrained leaders, or managing change. We are an aggressive, results-focused team of performance improvement professionals who refuse to believe "things can't be done". For us, failure is not an option. Our logo reflects a target from the view of the site on a gun.

In addition to the contact information provided on the sample business card (do not include "turning people problems into profits"), I would like to include this statement (probably on the back):
I equip results-oriented business leaders to turn their people problems into profits in six months or less.

PLEASE NOTE THAT MY WEBSITE IS UNDER REVISION TO TONE DOWN THE MILITARY THEME, ALTHOUGH THE WARRIOR ENERGY AND FOCUS ON RESULTS REMAINS.

Target Market(s)

My clients are Mid and senior-level managers. I don't target any particular industry.

Industry/Entity Type

Consulting

Contact Information for Business Card

In addition to the contact information provided on the sample business card (DO NOT INCLUDE "turning people problems into profits"), I would like to include this statement (probably on the back):

I don't care whether the card is landscape or portrait view.

Font styles to use
Sans Serif

Requirements
Must have
• 1. be easy to read, no 6-8 point fonts!
• 2. a "vibe" that captures the eye without being too chaotic or busy
• 3. bold color, not washed out or boring - a good blend with the colors currently on my website (black, red, white, army green) but you don't need to use all of them.
• 4. all the contact information I have provided
• 5. a good blend with the colors currently on my website
• 6. Must have this quote on the back of the card: I equip results-oriented business leaders to turn their people problems into profits in six months or less.
Nice to have
• In looking at the sample images I provided for ideas, you can see that I like the way a card carries over from one side to the next.
• It would be great to find some aspect/quality/feature that I haven't seen before
Should not have
• 1. NO use of ALL CAPS
• 2. fonts that I would have to seek out and purchase (you should provide files for font if using something not standard)

```html
<!DOCTYPE html>
<html lang="en">
<head>
<meta charset="utf-8">
<title>Brightmoor Lane – Business Card</title>
<link rel="stylesheet" href="https://fonts.googleapis.com/css2?family=Open+Sans:wdth,wght@75..100,300..800&display=swap">
<style>
  :root {
    --backdrop: #7b7b7b;
    --card-light: #ececec;
    --card-dark: #231f20;
    --olive: #3b3d2a;
    --signal-red: #e8392e;
    --ink: #333333;
    --white: #ffffff;
    --rule: #4a4a4a;
  }
  html, body {
    margin: 0;
    padding: 0;
    width: 1200px;
    height: 1200px;
    overflow: hidden;
    background: var(--backdrop);
    font-family: "Open Sans", Arial, sans-serif;
  }
  .canvas {
    position: relative;
    width: 1200px;
    height: 1200px;
  }
  .card {
    position: absolute;
    top: 310px;
    box-sizing: border-box;
    box-shadow: 2px 3px 6px rgba(0,0,0,0.35);
  }
  .card--front {
    left: 234px;
    width: 364px;
    height: 594px;
    background: var(--card-light);
    text-align: center;
    color: var(--ink);
  }
  .card--back {
    left: 627px;
    width: 370px;
    height: 595px;
    background: var(--card-dark);
    color: var(--white);
    text-align: center;
  }
  .brand-name {
    position: absolute;
    left: 0;
    right: 0;
    top: 128px;
    margin: 0;
    font-size: 34px;
    line-height: 42px;
    font-weight: 800;
    color: var(--olive);
  }
  .person {
    position: absolute;
    left: 0;
    right: 0;
    top: 316px;
  }
  .person__name {
    margin: 0;
    font-size: 19px;
    line-height: 26px;
    font-weight: 600;
    color: var(--olive);
  }
  .person__title {
    margin: 0;
    font-size: 17px;
    line-height: 22px;
    color: var(--signal-red);
  }
  .rule {
    position: absolute;
    left: 66px;
    top: 372px;
    width: 232px;
    height: 1px;
    margin: 0;
    border: 0;
    background: var(--rule);
  }
  .contact {
    position: absolute;
    left: 0;
    right: 0;
    top: 384px;
    margin: 0;
    padding: 0;
    list-style: none;
    font-size: 17px;
    line-height: 21.5px;
    color: var(--ink);
  }
  .contact__label { font-weight: 700; }
  .contact__web-accent { color: var(--signal-red); }
  .back-name {
    position: absolute;
    left: 0;
    right: 0;
    top: 272px;
    margin: 0;
    font-size: 34px;
    line-height: 42px;
    font-weight: 800;
    color: var(--white);
  }
  .promise {
    position: absolute;
    left: 0;
    right: 0;
    top: 390px;
    margin: 0;
    font-size: 17px;
    line-height: 21.5px;
    font-weight: 600;
    font-stretch: 78%;
    color: var(--white);
  }
  .back-web {
    position: absolute;
    left: 0;
    right: 0;
    top: 538px;
    margin: 0;
    font-size: 20px;
    font-weight: 700;
    letter-spacing: 1.5px;
    font-stretch: 85%;
  }
</style>
</head>
<body>
<main class="canvas">
  <section class="card card--front" aria-label="Card front">
    <h1 class="brand-name">Brightmoor Lane</h1>
    <div class="person">
      <p class="person__name">Dana Whitfield</p>
      <p class="person__title">Chief Performance Strategist</p>
    </div>
    <hr class="rule">
    <ul class="contact">
      <li><span class="contact__label">P:</span> 555-210-4418</li>
      <li><span class="contact__label">M:</span> 555-307-5926</li>
      <li><span class="contact__label">E:</span> danaw@brightmoorlane.com</li>
      <li>www.<span class="contact__web-accent">brightmoorlane</span>.com</li>
    </ul>
  </section>

  <section class="card card--back" aria-label="Card back">
    <p class="back-name">Brightmoor Lane</p>
    <p class="promise">I equip results-oriented business<br>leaders to turn their people problems<br>into profits in six months or less.</p>
    <p class="back-web">www.brightmoorlane.com</p>
  </section>
</main>
</body>
</html>
```